Prairie 2014 District Meeting

This flyer will be printed on a 4" x 6" flyer.

Requirements
Must have
• Flyer must be done in landscape format

Please use only 1 of the 3 uploaded skyline photos as a background

Zeta Kappa Chapter, Sigma Rho Tau Fraternity, Inc. Proudly Hosts the 64th Annual 5th District Meeting In Oklahoma City

April 17th - 20th 2014

Host Hotel: Halvorne, Oklahoma City (405) 555-0147

District Marshall: Bro. Curtis Fenley (405) 555-0193
Deputy District Marshall: Bro. Leon Pratt
Nice to have
• Purple & Gold are the fraternity's colors

```html
<!DOCTYPE html>
<html lang="en">
<head>
<meta charset="utf-8">
<title>Prairie 2014 District Meeting</title>
<link rel="stylesheet" href="https://fonts.googleapis.com/css2?family=Arimo:wght@400;700&family=Open+Sans:wght@600;700&display=swap">
<style>
  :root {
    --page: #2a1a16;
    --ink: #0b0b0d;
    --green: #5cb947;
    --purple: #8a4a9e;
    --purple-deep: #7a3f8e;
    --white: #ffffff;
  }
  * { margin: 0; padding: 0; box-sizing: border-box; }
  html, body { width: 1200px; height: 847px; overflow: hidden; background: var(--page); }
  .flyer {
    position: absolute; left: 0; top: 23.5px;
    width: 1200px; height: 800px;
    background: var(--ink);
    overflow: hidden;
    font-family: "Arimo", Arial, sans-serif;
  }
  .city-backdrop {
    position: absolute; inset: 0;
    background:
      radial-gradient(ellipse at 30% 60%, rgba(150,150,150,.28), transparent 60%),
      linear-gradient(180deg, #050507 0%, #1b1b1e 35%, #2c2c2f 70%, #1a1a1c 100%);
  }
  .artwork { position: absolute; inset: 0; }
  .brand {
    position: absolute; left: 40px; top: 110px; width: 235px;
    display: flex; align-items: center; gap: 10px;
    color: var(--green); font-weight: 700; font-size: 22px; line-height: 1.1;
  }
  .brand-dot { width: 26px; height: 26px; border-radius: 50%; background: var(--purple); flex: none; }
  .headline { position: absolute; left: 291px; top: 38px; color: var(--white); }
  .headline .chapter { font-weight: 700; font-size: 21px; color: var(--green); }
  .headline .hosts { font-family: "Open Sans", sans-serif; font-weight: 600; font-size: 26px; margin-top: 10px; letter-spacing: -.2px; }
  .headline .city { font-family: "Open Sans", sans-serif; font-weight: 700; font-size: 30px; margin-top: 6px; }
  .details { position: absolute; left: 37px; top: 455px; color: var(--green); }
  .details .label { font-weight: 700; font-size: 21px; }
  .details .date { font-weight: 700; font-size: 30px; line-height: 1.22; margin-top: 8px; }
  .details .hotel-label { margin-top: 36px; }
  .details .hotel { font-size: 26px; margin-top: 4px; }
  .details .phone { font-weight: 700; font-size: 29px; margin-top: 6px; }
  .officers-band {
    position: absolute; left: 0; top: 712px; width: 1200px; height: 88px;
    background: var(--purple); color: var(--white); font-weight: 700;
  }
  .officer { position: absolute; top: 12px; }
  .officer .title { font-size: 21px; }
  .officer .name { font-size: 27px; margin-top: 8px; }
  .officer.marshal { left: 39px; }
  .officer.marshal .title { padding-left: 283px; }
  .officer.deputy { left: 682px; }
</style>
</head>
<body>
<main class="flyer">
  <div class="city-backdrop" role="img" aria-label="Night aerial view of the Oklahoma City skyline, darkened as a backdrop"></div>

  <svg class="artwork" width="1200" height="800" viewBox="0 0 1200 800">
    <defs>
      <radialGradient id="skyline-glow" cx="55%" cy="60%" r="65%">
        <stop offset="0" stop-color="#c98a3a"/>
        <stop offset=".45" stop-color="#5a4a6a"/>
        <stop offset=".8" stop-color="#1f2038"/>
        <stop offset="1" stop-color="#0e1024"/>
      </radialGradient>
    </defs>
    <ellipse cx="719" cy="430" rx="375" ry="246" fill="url(#skyline-glow)" role="img" aria-label="Night photograph of downtown Oklahoma City skyline with lit towers"/>
    <path class="swoosh-purple" fill="var(--purple)" d="M617,157 C380,200 200,330 225,470 C250,620 450,720 700,712 C950,705 1130,560 1179,430 C1100,590 900,690 700,690 C480,690 330,560 345,420 C360,300 470,200 617,157 Z"/>
    <path class="swoosh-green" fill="var(--green)" d="M468,270 C560,180 720,130 860,135 C1050,140 1200,230 1190,370 C1180,500 1000,610 810,639 C980,590 1130,500 1120,380 C1110,250 980,180 820,175 C690,172 560,210 468,270 Z"/>
  </svg>

  <div class="brand"><span class="brand-dot"></span><span>Sigma Rho Tau</span></div>

  <header class="headline">
    <p class="chapter">Zeta Kappa Chapter, Sigma Rho Tau Fraternity, Inc.</p>
    <p class="hosts">Proudly Hosts the 64th Annual 5th District Meeting In</p>
    <p class="city">OKLAHOMA CITY</p>
  </header>

  <section class="details">
    <p class="label">Date:</p>
    <p class="date">April 17th -<br>20th 2014</p>
    <p class="label hotel-label">Host Hotel:</p>
    <p class="hotel">Halvorne, Oklahoma City</p>
    <p class="phone">(405) 555-0147</p>
  </section>

  <footer class="officers-band">
    <div class="officer marshal">
      <p class="title">District Marshall</p>
      <p class="name">Bro. Curtis Fenley - (405) 555-0193</p>
    </div>
    <div class="officer deputy">
      <p class="title">Deputy District Marshall:</p>
      <p class="name">Bro. Leon Pratt</p>
    </div>
  </footer>
</main>
</body>
</html>
```